business cards, stationary
lets see what you got
Use specific fonts
up to designer
Modern
Calvin Marsh
Director of Sales
1870 Quarrymill road, Suite 114 Burlington, On L4K 3P8
Calvin@sunlanejourneys.example
www.sunlanejourneys.example
BBM: 58720936
LOGO on back

```html
<!DOCTYPE html>
<html lang="en">
<head>
<meta charset="utf-8">
<title>Calvin Marsh – Business Cards</title>
<link href="https://fonts.googleapis.com/css2?family=Open+Sans:wght@400;600;700&display=swap" rel="stylesheet">
<style>
  :root {
    --bg: #e9e9e9;
    --card-white: #ffffff;
    --green: #8cc63f;
    --green-dark: #6fae2a;
    --green-light: #a6d45e;
    --purple: #5e2d79;
    --purple-card: #6a3d86;
    --grey-text: #555555;
    --ink: #333333;
  }
  * { margin: 0; padding: 0; box-sizing: border-box; }
  html, body { width: 1200px; height: 1037px; overflow: hidden; }
  body {
    background: var(--bg);
    font-family: "Open Sans", Arial, sans-serif;
    position: relative;
  }
  .card {
    position: absolute;
    width: 495px;
    height: 295px;
    border-radius: 14px;
    overflow: hidden;
    box-shadow: 0 4px 14px rgba(0,0,0,0.18);
  }
  .card--front { left: 93px; top: 205px; background: var(--card-white); }
  .card--green { left: 618px; top: 205px; background: radial-gradient(circle at 45% 40%, var(--green-light), var(--green) 70%); }
  .card--purple { left: 93px; top: 540px; background: radial-gradient(circle at 45% 40%, #7a4d96, var(--purple-card) 70%); }
  .card--white { left: 618px; top: 540px; background: var(--card-white); }

  .wordmark {
    position: absolute;
    display: flex;
    align-items: center;
    gap: 8px;
    font-weight: 700;
    letter-spacing: -0.3px;
  }
  .wordmark__dot { width: 16px; height: 16px; border-radius: 50%; }
  .front-mark { left: 24px; top: 46px; font-size: 22px; color: var(--purple); }
  .front-mark .wordmark__dot { background: var(--green); }
  .centre-mark { left: 0; right: 0; top: 128px; justify-content: center; font-size: 30px; }
  .card--green .centre-mark, .card--purple .centre-mark { color: #ffffff; }
  .card--green .wordmark__dot, .card--purple .wordmark__dot { background: rgba(255,255,255,0.85); }
  .card--white .centre-mark { color: var(--purple); }
  .card--white .wordmark__dot { background: var(--green); }

  .faint-disc {
    position: absolute;
    left: 150px; top: 20px;
    width: 200px; height: 200px;
    border-radius: 50%;
    background: rgba(255,255,255,0.12);
  }
  .card--white .faint-disc { background: rgba(140,198,63,0.12); left: 110px; top: 60px; }

  .holder { position: absolute; left: 293px; top: 44px; }
  .holder__name { font-size: 21px; font-weight: 700; color: var(--purple); line-height: 1.1; }
  .holder__title { font-size: 13px; color: var(--grey-text); margin-top: 2px; }

  .contact {
    position: absolute; left: 290px; top: 128px;
    list-style: none;
    font-size: 10.5px; color: var(--ink);
  }
  .contact__item { display: flex; align-items: center; gap: 9px; height: 17px; white-space: nowrap; }
  .contact__icon { width: 11px; height: 11px; fill: var(--ink); flex: none; }
  .contact__label { font-weight: 700; width: 11px; font-size: 8px; flex: none; }
  .contact__address { margin-top: 8px; line-height: 1.4; }

  .front-art {
    position: absolute;
    left: 0; bottom: 0;
    width: 265px; height: 118px;
    border-top-right-radius: 100% 60%;
    background: linear-gradient(170deg, var(--purple) 0 14%, var(--green-light) 14% 45%, var(--green) 80%, var(--green-dark));
  }
</style>
</head>
<body>

<section class="card card--front" aria-label="Card front">
  <div class="wordmark front-mark"><span class="wordmark__dot"></span>sunlanejourneys</div>
  <div class="holder">
    <div class="holder__name">Calvin Marsh</div>
    <div class="holder__title">Director of Sales</div>
  </div>
  <ul class="contact">
    <li class="contact__item"><svg class="contact__icon" viewBox="0 0 12 12"><rect x="3" y="0.5" width="6" height="11" rx="1.2"/></svg>705.555.0142</li>
    <li class="contact__item"><svg class="contact__icon" viewBox="0 0 12 12"><path d="M2 1l2.5-.5 1.5 3-1.5 1c.7 1.5 1.7 2.5 3.2 3.2l1-1.5 3 1.5-.5 2.5C6 10.5 1.5 6 2 1z"/></svg>1.877.555.0178</li>
    <li class="contact__item"><svg class="contact__icon" viewBox="0 0 12 12"><path d="M0.5 2.5h11v7h-11z M0.5 2.5l5.5 4 5.5-4" fill="none" stroke="#333" stroke-width="1.3"/></svg>Calvin@sunlanejourneys.example</li>
    <li class="contact__item"><svg class="contact__icon" viewBox="0 0 12 12"><circle cx="6" cy="6" r="5" fill="none" stroke="#333" stroke-width="1.2"/><path d="M1 6h10M6 1c-2.5 3-2.5 7 0 10M6 1c2.5 3 2.5 7 0 10" fill="none" stroke="#333" stroke-width="0.9"/></svg>www.sunlanejourneys.example</li>
    <li class="contact__item"><span class="contact__label">BBM</span>58720936</li>
    <li class="contact__address">1870 Quarrymill road,<br>Suite 114, Burlington, On L4K 3P8</li>
  </ul>
  <div class="front-art" role="img" aria-label="Decorative green leaf shape with a purple swoosh"></div>
</section>

<section class="card card--green" aria-label="Card back, green">
  <div class="faint-disc"></div>
  <div class="wordmark centre-mark"><span class="wordmark__dot"></span>sunlanejourneys</div>
</section>

<section class="card card--purple" aria-label="Card back, purple">
  <div class="faint-disc"></div>
  <div class="wordmark centre-mark"><span class="wordmark__dot"></span>sunlanejourneys</div>
</section>

<section class="card card--white" aria-label="Card back, white">
  <div class="faint-disc"></div>
  <div class="wordmark centre-mark"><span class="wordmark__dot"></span>sunlanejourneys</div>
</section>

</body>
</html>
```